Gardener needs an exciting new flyer design.

I'm a passionate gardener that requires a custom flyer design for a owner operator gardening business. Design will be for a DL flyer. I'm based on the Sunshine coast in Queensland Australia. My target audience is the residential market on the Sunshine coast. Business name is Marlowe Greens. My services are, lawn mowing, weeding, Eco Friendly fertilizing, green waste removal, Mulching, tree and shrub pruning, Full garden makeovers, hedging, pressure cleaning, privacy screening, Timber deck rejuvenation, Planting, Turf preparation and installation, and much more. Free no obligation quotes, reliable and friendly service, great rates. 12 years experience. Web www.marlowegreens.com.au - Phone 0418527064 - Email doug@marlowegreens.com.au I would like the design to portray a friendly and professional approach.

Target Market(s)

Residential

Industry/Entity Type

Gardener

Font styles to use
Serif

Colors
9ccb3b
abd037
3176b5

Requirements
Must have
• my services, my logo, my contact details,

```html
<!DOCTYPE html>
<html lang="en">
<head>
<meta charset="utf-8">
<title>Marlowe Greens – DL Flyer</title>
<link href="https://fonts.googleapis.com/css2?family=Roboto+Slab:wght@700;800&family=Open+Sans:wght@400;600&display=swap" rel="stylesheet">
<style>
  :root {
    --backdrop: #8c8c8c;
    --paper: #ffffff;
    --purple: #5e2363;
    --green: #3a9a2a;
    --green-light: #9ccb3b;
    --lime: #abd037;
    --ink: #3a3a3a;
  }
  * { box-sizing: border-box; margin: 0; padding: 0; }
  html, body { width: 1200px; height: 1200px; overflow: hidden; }
  body {
    background: var(--backdrop);
    font-family: "Open Sans", sans-serif;
    position: relative;
  }
  .flyer {
    position: absolute;
    top: 138px;
    width: 440px;
    height: 924px;
    background: var(--paper);
    overflow: hidden;
    box-shadow: 0 6px 18px rgba(0,0,0,.25);
  }
  .flyer--front { left: 140px; }
  .flyer--back { left: 620px; }
  .flyer svg.artwork { position: absolute; inset: 0; width: 440px; height: 924px; }
  .brand {
    position: absolute; top: 52px; left: 0; width: 100%;
    display: flex; justify-content: center; align-items: center; gap: 10px;
    font-family: "Roboto Slab", serif; font-weight: 700; font-size: 30px; color: var(--green);
  }
  .brand__dot { width: 14px; height: 14px; border-radius: 50%; background: var(--purple); }
  .headline {
    position: absolute; top: 286px; left: 20px; width: 400px; text-align: center;
    font-family: "Roboto Slab", serif; font-weight: 800; font-size: 22px; line-height: 1.25;
    color: #fff; text-shadow: 0 1px 3px rgba(0,0,0,.35); text-transform: uppercase;
  }
  .welcome {
    position: absolute; top: 566px; left: 0; width: 100%; text-align: center;
    font-family: "Roboto Slab", serif; font-weight: 800; font-size: 26px; line-height: 1.15;
    color: var(--purple); text-transform: uppercase;
  }
  .intro {
    position: absolute; top: 642px; left: 50px; width: 340px; text-align: center;
    font-size: 12px; line-height: 1.4; color: var(--ink);
  }
  .intro p + p { margin-top: 10px; }
  .web-strip {
    position: absolute; bottom: 30px; left: 0; width: 100%; text-align: center;
    font-weight: 600; font-size: 20px; color: #fff; letter-spacing: .5px;
  }
  .section-title {
    position: absolute; left: 0; width: 100%; text-align: center;
    font-family: "Roboto Slab", serif; font-weight: 800; font-size: 24px;
    color: var(--purple); text-transform: uppercase;
  }
  .section-title--garden { top: 336px; }
  .section-title--other { top: 566px; }
  .service-list {
    position: absolute; list-style: none;
    font-size: 13px; line-height: 1.25; color: var(--ink);
  }
  .service-list li { display: flex; gap: 7px; margin-bottom: 10px; }
  .service-list svg { flex: none; width: 12px; height: 12px; margin-top: 2px; }
  .list-garden-a { top: 384px; left: 40px; width: 180px; }
  .list-garden-b { top: 384px; left: 225px; width: 190px; }
  .list-other-a { top: 614px; left: 40px; width: 180px; }
  .list-other-b { top: 614px; left: 225px; width: 190px; }
  .contact {
    position: absolute; top: 778px; left: 0; width: 100%;
    list-style: none; text-align: center; color: #fff; font-size: 17px;
  }
  .contact li { display: flex; justify-content: center; align-items: center; gap: 8px; margin-bottom: 8px; }
  .contact__phone { font-size: 20px; }
  .contact svg { width: 14px; height: 14px; }
</style>
</head>
<body>

<section class="flyer flyer--front">
  <svg class="artwork" viewBox="0 0 440 924">
    <defs>
      <linearGradient id="gardenScene" x1="0" y1="0" x2="0" y2="1">
        <stop offset="0" stop-color="#e9eef0"/>
        <stop offset="0.3" stop-color="#5e8a3a"/>
        <stop offset="0.55" stop-color="#4f8a2e"/>
        <stop offset="0.75" stop-color="#3fa52a"/>
        <stop offset="1" stop-color="#5cc232"/>
      </linearGradient>
    </defs>
    <path role="img" aria-label="Photo of a manicured lawn with colourful flower beds and trees"
          d="M0 140 H440 V400 Q220 470 0 540 Z" fill="url(#gardenScene)"/>
    <path d="M0 548 Q220 478 440 408" fill="none" stroke="var(--green)" stroke-width="8"/>
    <path d="M0 558 Q220 488 440 418" fill="none" stroke="var(--lime)" stroke-width="3"/>
    <path d="M0 924 V860 Q220 855 440 815 V924 Z" fill="var(--purple)"/>
    <path d="M0 852 Q220 847 440 807" fill="none" stroke="var(--green)" stroke-width="7"/>
    <path d="M0 844 Q220 839 440 799" fill="none" stroke="var(--lime)" stroke-width="2"/>
  </svg>
  <div class="brand"><span class="brand__dot"></span>Marlowe Greens</div>
  <h2 class="headline">A beautiful garden<br>doesn't happen by itself</h2>
  <h1 class="welcome">Welcome to<br>Marlowe Greens</h1>
  <div class="intro">
    <p>Marlowe Greens is your garden &amp; lawn care specialist, with a passion for gardening and a keen eye for detail you can rest assured you're in the right hands.</p>
    <p>My services are tailored to meet every individual clients needs. From a one time mow to regular lawn mowing, all aspects of garden care and even full garden makeovers.</p>
    <p>I go that extra mile every time to leave your garden and yard looking amazing.</p>
  </div>
  <div class="web-strip">www.marlowegreens.com.au</div>
</section>

<section class="flyer flyer--back">
  <svg class="artwork" viewBox="0 0 440 924">
    <defs>
      <linearGradient id="houseScene" x1="0" y1="0" x2="0" y2="1">
        <stop offset="0" stop-color="#2f8fe0"/>
        <stop offset="0.35" stop-color="#9fcdf0"/>
        <stop offset="0.55" stop-color="#d9d2bd"/>
        <stop offset="0.7" stop-color="#4f8f2e"/>
        <stop offset="1" stop-color="#6cbf3a"/>
      </linearGradient>
    </defs>
    <path role="img" aria-label="Photo of a tidy suburban house with green lawn, shrubs and driveway"
          d="M0 0 H440 V250 Q220 290 0 360 Z" fill="url(#houseScene)"/>
    <path d="M0 368 Q220 298 440 258" fill="none" stroke="var(--green)" stroke-width="8"/>
    <path d="M0 378 Q220 308 440 268" fill="none" stroke="var(--lime)" stroke-width="3"/>
    <path d="M0 924 V760 Q220 750 440 700 V924 Z" fill="var(--purple)"/>
    <path d="M0 752 Q220 742 440 692" fill="none" stroke="var(--green)" stroke-width="7"/>
    <path d="M0 744 Q220 734 440 684" fill="none" stroke="var(--lime)" stroke-width="2"/>
  </svg>

  <h2 class="section-title section-title--garden">Garden Services</h2>
  <ul class="service-list list-garden-a">
    <li><svg viewBox="0 0 12 12"><path d="M1 6 L4.5 9.5 L11 2" fill="none" stroke="var(--green)" stroke-width="2"/></svg>Lawn mowing</li>
    <li><svg viewBox="0 0 12 12"><path d="M1 6 L4.5 9.5 L11 2" fill="none" stroke="var(--green)" stroke-width="2"/></svg>Fertilizing</li>
    <li><svg viewBox="0 0 12 12"><path d="M1 6 L4.5 9.5 L11 2" fill="none" stroke="var(--green)" stroke-width="2"/></svg>Garden mulching</li>
    <li><svg viewBox="0 0 12 12"><path d="M1 6 L4.5 9.5 L11 2" fill="none" stroke="var(--green)" stroke-width="2"/></svg>Hedging</li>
    <li><svg viewBox="0 0 12 12"><path d="M1 6 L4.5 9.5 L11 2" fill="none" stroke="var(--green)" stroke-width="2"/></svg>Weeding</li>
  </ul>
  <ul class="service-list list-garden-b">
    <li><svg viewBox="0 0 12 12"><path d="M1 6 L4.5 9.5 L11 2" fill="none" stroke="var(--green)" stroke-width="2"/></svg>Turf preparation and installation</li>
    <li><svg viewBox="0 0 12 12"><path d="M1 6 L4.5 9.5 L11 2" fill="none" stroke="var(--green)" stroke-width="2"/></svg>Tree and shrub pruning</li>
    <li><svg viewBox="0 0 12 12"><path d="M1 6 L4.5 9.5 L11 2" fill="none" stroke="var(--green)" stroke-width="2"/></svg>Full garden makeovers</li>
    <li><svg viewBox="0 0 12 12"><path d="M1 6 L4.5 9.5 L11 2" fill="none" stroke="var(--green)" stroke-width="2"/></svg>Green waste removal</li>
  </ul>

  <h2 class="section-title section-title--other">Other Services</h2>
  <ul class="service-list list-other-a">
    <li><svg viewBox="0 0 12 12"><path d="M1 6 L4.5 9.5 L11 2" fill="none" stroke="var(--green)" stroke-width="2"/></svg>Aluminium fencing &amp; gate installation &amp; repairs</li>
    <li><svg viewBox="0 0 12 12"><path d="M1 6 L4.5 9.5 L11 2" fill="none" stroke="var(--green)" stroke-width="2"/></svg>Pressure cleaning</li>
  </ul>
  <ul class="service-list list-other-b">
    <li><svg viewBox="0 0 12 12"><path d="M1 6 L4.5 9.5 L11 2" fill="none" stroke="var(--green)" stroke-width="2"/></svg>Timber decking rejuvenation and repairs</li>
    <li><svg viewBox="0 0 12 12"><path d="M1 6 L4.5 9.5 L11 2" fill="none" stroke="var(--green)" stroke-width="2"/></svg>And much more!</li>
  </ul>

  <ul class="contact">
    <li class="contact__phone"><svg viewBox="0 0 14 14"><path d="M3 1 L5.5 1 L6.5 4 L5 5.2 Q6.3 8 8.8 9 L10 7.5 L13 8.5 L13 11 Q12 13 10 13 Q1 11 1 3 Q1 1 3 1 Z" fill="var(--green-light)"/></svg>0418527064</li>
    <li><svg viewBox="0 0 14 14"><rect x="1" y="3" width="12" height="8" rx="1" fill="var(--green-light)"/><path d="M1.5 3.5 L7 8 L12.5 3.5" fill="none" stroke="var(--purple)" stroke-width="1.2"/></svg>doug@marlowegreens.com.au</li>
    <li><svg viewBox="0 0 14 14"><circle cx="7" cy="7" r="6" fill="var(--green-light)"/><path d="M1 7 H13 M7 1 Q3.5 7 7 13 M7 1 Q10.5 7 7 13" fill="none" stroke="var(--purple)" stroke-width="1"/></svg>www.marlowegreens.com.au</li>
  </ul>
</section>

</body>
</html>
```